Business Card Design needed for logo design project

This project is linked to a href='http://jobs.pixelfennel.example/job.aspx?id=412907'Tide Nook: Design a logo for our new trailer boat syndication business in Sydney
Our company needs a Business Card Design. Please refer to our original project in the link above.
I would like a relatively simple and classy business card design. could you please also use small symbols for identifying contact info eg. mobile, web and email?
Updates
Please see my new project to design a business card for a trailer boat syndication business in Sydney, Australia.
Industry/Entity Type
Business
Look and feel
Each slider illustrates characteristics of the customer's brand and the style your logo design should communicate.

```html
<!DOCTYPE html>
<html lang="en">
<head>
<meta charset="utf-8">
<title>Tide Nook — Business Card</title>
<link rel="stylesheet" href="https://fonts.googleapis.com/css2?family=Exo+2:wght@700&family=Tinos&display=swap">
<style>
  :root {
    --backdrop-light: #d9d9d9;
    --backdrop-dark: #8a8a8a;
    --teal: #33aebb;
    --charcoal: #353535;
    --white: #ffffff;
    --soft-white: #f2f2f2;
  }
  * { box-sizing: border-box; margin: 0; padding: 0; }
  html, body { width: 1200px; height: 900px; overflow: hidden; }
  body {
    background: radial-gradient(ellipse at 50% 70%, var(--backdrop-light) 0%, #b8b8b8 55%, var(--backdrop-dark) 100%);
    position: relative;
  }
  .card {
    position: absolute;
    top: 300px;
    width: 525px;
    height: 300px;
    border-radius: 3px;
    box-shadow: 0 14px 30px rgba(0,0,0,.28);
  }
  .card--front { left: 50px; background: var(--teal); }
  .card--back { left: 625px; background: var(--charcoal); }

  .brand { display: flex; align-items: center; gap: 12px; }
  .brand__dot { width: 22px; height: 22px; border-radius: 50%; flex: none; }
  .brand__name {
    font-family: "Exo 2", sans-serif;
    font-weight: 700;
    line-height: 1;
  }
  .tagline {
    font-family: "Exo 2", sans-serif;
    font-weight: 700;
    font-size: 9.5px;
    letter-spacing: 1.2px;
    text-transform: uppercase;
  }

  .card--front .brand { position: absolute; left: 70px; top: 118px; }
  .card--front .brand__dot { background: var(--white); }
  .card--front .brand__name { color: var(--white); font-size: 40px; }
  .card--front .tagline { position: absolute; left: 104px; top: 166px; color: var(--white); }

  .card--back .brand { position: absolute; left: 0; right: 0; top: 58px; justify-content: center; }
  .card--back .brand__dot { background: var(--teal); }
  .card--back .brand__name { color: var(--teal); font-size: 44px; }
  .card--back .tagline { position: absolute; left: 0; right: 0; top: 112px; text-align: center; color: var(--soft-white); font-size: 9px; }

  .contacts { position: absolute; left: 150px; top: 168px; list-style: none; }
  .contact {
    display: flex; align-items: center; gap: 12px;
    font-family: "Tinos", serif;
    font-size: 16px;
    height: 27px;
  }
  .contact__icon { width: 16px; height: 16px; flex: none; }
  .contact__label { color: var(--teal); }
  .contact__value { color: var(--white); }
</style>
</head>
<body>
  <section class="card card--front" aria-label="Business card front">
    <div class="brand">
      <span class="brand__dot"></span>
      <span class="brand__name">TideNook.com.au</span>
    </div>
    <p class="tagline">Trailer boat syndication and management</p>
  </section>

  <section class="card card--back" aria-label="Business card back">
    <div class="brand">
      <span class="brand__dot"></span>
      <span class="brand__name">Tide Nook</span>
    </div>
    <p class="tagline">Trailer boat syndication and management</p>

    <ul class="contacts">
      <li class="contact">
        <svg class="contact__icon" viewBox="0 0 16 16" fill="none" stroke="#33aebb" stroke-width="1.2">
          <circle cx="8" cy="8" r="6.5"/><ellipse cx="8" cy="8" rx="3" ry="6.5"/><path d="M1.5 8h13M2.5 4.8h11M2.5 11.2h11"/>
        </svg>
        <span class="contact__label">Web:</span><span class="contact__value">sample.com</span>
      </li>
      <li class="contact">
        <svg class="contact__icon" viewBox="0 0 16 16">
          <rect x="1" y="3.5" width="14" height="9" fill="#33aebb"/><path d="M1 3.5l7 5 7-5" fill="none" stroke="#353535" stroke-width="1.2"/>
        </svg>
        <span class="contact__label">Email:</span><span class="contact__value">sample@mailbox.example</span>
      </li>
      <li class="contact">
        <svg class="contact__icon" viewBox="0 0 16 16" fill="#33aebb">
          <path d="M1 5.5c0-1.5 3-2.5 7-2.5s7 1 7 2.5v1.2h-3.2V5.3c-1-.4-2.4-.6-3.8-.6s-2.8.2-3.8.6v1.4H1z"/>
          <path d="M3.5 8h9l1.5 5.5H2z"/><circle cx="8" cy="10.6" r="1.5" fill="#353535"/>
        </svg>
        <span class="contact__label">Tell:</span><span class="contact__value">999 9999</span>
      </li>
    </ul>
  </section>
</body>
</html>
```